Wordpress Design Project - MarbleQuay

I would like our existing old website at www.marblequay.example to be redesigned to a more modern attractive site using Wordpress, a total of 5 web pages. And also installed onto our new web hosting site. Please visit the existing website using Microsoft Internet explorer to see the content.
The new site must be compatible with all popular web browsers and mobile devices (if possible).
There should be a contact button available on each page with an associated form in case an interested person wants to contact us. This form must be spam proof not allowing automated crawlers from activating it.

There are only 5 pages web pages to this MarbleQuay project.

```html
<!DOCTYPE html>
<html lang="en">
<head>
<meta charset="utf-8">
<title>MarbleQuay – Telephone VoIP Solutions</title>
<link href="https://fonts.googleapis.com/css2?family=Anton&family=Arimo:wght@400;700&family=Open+Sans:wght@400;600&display=swap" rel="stylesheet">
<style>
  :root{
    --ink:#3a3a3c;
    --brand:#1d5fa8;
    --brand-dark:#0e3f80;
    --accent:#1aa3e0;
    --nav-bg:#e6e6e8;
    --hero-glow:#b9e6fb;
    --footer-bg:#e6e7e9;
    --field-line:#c8c8c8;
    --placeholder:#cfcfcf;
    --social:#8a8a8c;
  }
  *{margin:0;padding:0;box-sizing:border-box}
  html,body{width:868px;height:1200px;overflow:hidden;background:#fff}
  body{position:relative;font-family:"Arimo",Arial,sans-serif;color:var(--ink)}
  .abs{position:absolute}
  .display{font-family:"Anton",Impact,sans-serif;font-weight:400;color:var(--ink);letter-spacing:.2px}

  /* header */
  .brand{left:113px;top:16px;display:flex;align-items:center;gap:10px}
  .brand-mark{width:36px;height:36px;background:var(--brand)}
  .brand-name{font-family:"Arimo",Arial,sans-serif;font-weight:700;font-size:22px;color:var(--brand)}
  .tollfree{left:580px;top:38px;width:140px;text-align:center}
  .tollfree .label{font-family:"Anton",Impact,sans-serif;font-size:15px;color:var(--ink);line-height:18px}
  .tollfree .number{font-family:"Open Sans",Arial,sans-serif;font-size:14px;color:#222;line-height:18px}

  /* nav */
  .nav{left:0;top:88px;width:868px;height:28px;background:var(--nav-bg)}
  .nav a{position:absolute;top:7px;font-family:"Anton",Impact,sans-serif;font-size:11.5px;color:var(--ink);text-decoration:none;letter-spacing:.3px}

  /* hero */
  .hero{left:0;top:116px;width:868px;height:170px;
    background:radial-gradient(ellipse 62% 95% at 50% 45%,var(--hero-glow) 0%,#d9f1fd 55%,#fff 100%);
    box-shadow:0 3px 5px rgba(0,0,0,.12)}
  .hero-title{left:111px;top:140px;font-size:32px;line-height:36px}
  .hero-text{left:111px;top:184px;width:220px;font-size:12.5px;line-height:14px;text-transform:uppercase;color:#333}
  .service{display:flex;align-items:center;gap:8px}
  .service svg{width:60px;height:60px;flex:none}
  .service .name{font-family:"Anton",Impact,sans-serif;font-size:15px;line-height:16px;color:var(--ink)}
  .service .name small{display:block;font-size:10.5px;line-height:12px}

  /* slider */
  .slide-title{left:147px;top:340px;font-size:23px;line-height:28px;width:230px}
  .slide-photo{left:422px;top:334px;width:242px;height:135px;
    background:radial-gradient(ellipse at 50% 45%,#2e6fbf 0%,#123a78 45%,#05122a 100%)}
  .slide-arrow{top:372px;width:10px;height:74px}

  /* products */
  .section-title{font-size:19px;line-height:22px}
  .products{left:108px;top:528px;width:441px;height:410px;border-right:1px dashed var(--accent)}
  .product{position:absolute;left:0;width:440px}
  .product .thumb{position:absolute;left:0;width:95px;height:95px;
    background:linear-gradient(160deg,#f4f4f2 0%,#dcdcda 45%,#3b3d3f 70%,#cfcfcc 100%)}
  .product h3{position:absolute;left:100px;top:0;font-family:"Anton",Impact,sans-serif;font-weight:400;font-size:14.5px;color:var(--ink)}
  .product p{position:absolute;left:100px;top:24px;width:320px;font-size:11.6px;line-height:14.3px;color:#111}
  .product .more{position:absolute;right:36px;font-size:11.6px;color:var(--accent);text-decoration:none}
  .product .rule{position:absolute;left:0;width:440px;border-top:1px dashed var(--accent)}

  /* sidebar */
  .sidebar{left:570px;top:528px;width:170px}
  .articles{list-style:none;margin-top:10px}
  .articles li{position:relative;font-size:11.6px;line-height:12px;margin-bottom:12.5px;color:#111;text-indent:16px}
  .articles li::before{content:"";position:absolute;left:2px;top:2px;border-left:6px solid var(--accent);border-top:4px solid transparent;border-bottom:4px solid transparent}
  .social{display:flex;gap:6px}
  .social span{width:22px;height:22px;border-radius:4px;background:var(--social)}
  .field{width:152px;height:23px;border:2px solid var(--field-line);margin-bottom:7px;padding:3px 4px;
    font-family:"Anton",Impact,sans-serif;font-size:12.5px;color:var(--placeholder);line-height:14px}
  .send{margin-left:100px;width:53px;height:23px;background:var(--brand);color:#fff;text-align:center;
    font-family:"Anton",Impact,sans-serif;font-size:14px;line-height:23px}

  /* footer */
  .texture{left:0;top:953px;width:868px;height:77px;background:linear-gradient(#f9f9f9,#f3f4f5)}
  .footer{left:0;top:1030px;width:868px;height:170px;background:var(--footer-bg);border-top:1px dashed var(--accent)}
  .f-col{position:absolute;top:45px}
  .f-col h4{font-family:"Arimo",Arial,sans-serif;font-weight:700;font-size:8.5px;color:#111;margin-bottom:3px}
  .f-col li{list-style:none;font-size:6.3px;line-height:7.8px;color:#111}
  .f-social{position:absolute;left:630px;top:66px;display:flex;gap:4px}
  .f-social span{width:16px;height:16px;border-radius:3px;background:#9a9a9c}
  .copyright{position:absolute;left:0;top:145px;width:868px;text-align:center;font-size:6.5px;color:#111}
</style>
</head>
<body>

<header>
  <div class="abs brand"><span class="brand-mark"></span><span class="brand-name">MarbleQuay</span></div>
  <div class="abs tollfree"><div class="label">CONTACT TOLL FREE</div><div class="number">1.800.555.0142</div></div>
  <nav class="abs nav">
    <a style="left:164px">HOME</a>
    <a style="left:232px">ABOUT US</a>
    <a style="left:324px">SOLUTIONS</a>
    <a style="left:416px">SUPPORT SERVICES</a>
    <a style="left:529px">CONTACT US</a>
  </nav>
</header>

<section class="abs hero"></section>
<h1 class="abs display hero-title">WHAT WE DO?</h1>
<p class="abs hero-text">MarbleQuay provides complete telephone VoIP PBX solutions for businesses large and small.</p>

<div class="abs service" style="left:353px;top:126px">
  <svg viewBox="0 0 60 60"><rect x="10" y="10" width="40" height="40" rx="7" transform="rotate(45 30 30)" fill="var(--brand)"/><rect x="21" y="19" width="18" height="22" rx="2" fill="#fff"/><rect x="24" y="22" width="12" height="4" fill="var(--accent)"/><g fill="var(--brand)"><rect x="24" y="29" width="3" height="3"/><rect x="29" y="29" width="3" height="3"/><rect x="34" y="29" width="2" height="3"/><rect x="24" y="34" width="3" height="3"/><rect x="29" y="34" width="3" height="3"/><rect x="34" y="34" width="2" height="3"/></g></svg>
  <div class="name">TELEPHONE VoIP<small>SOLUTION</small></div>
</div>
<div class="abs service" style="left:555px;top:130px">
  <svg viewBox="0 0 60 60"><rect x="10" y="10" width="40" height="40" rx="7" transform="rotate(45 30 30)" fill="var(--brand)"/><g stroke="#fff" stroke-width="1.5" fill="none"><path d="M26 24 L32 30 L26 36 M32 30 H38"/></g><g fill="#fff"><rect x="21" y="20" width="8" height="6"/><rect x="21" y="34" width="8" height="6"/><rect x="36" y="27" width="8" height="6"/></g></svg>
  <div class="name">IP, LAN AND<small>INTERNET</small></div>
</div>
<div class="abs service" style="left:353px;top:212px">
  <svg viewBox="0 0 60 60"><rect x="10" y="10" width="40" height="40" rx="7" transform="rotate(45 30 30)" fill="var(--brand)"/><path d="M20 20 H36 V31 H26 L22 35 V31 H20 Z" fill="#fff"/><path d="M30 33 H40 V26 H38 V35 H33 Z" fill="#fff" opacity=".8"/></svg>
  <div class="name">SUPPORT SERVICES</div>
</div>
<div class="abs service" style="left:558px;top:212px">
  <svg viewBox="0 0 60 60"><rect x="10" y="10" width="40" height="40" rx="7" transform="rotate(45 30 30)" fill="var(--brand)"/><ellipse cx="30" cy="29" rx="11" ry="7" fill="#fff"/><path d="M23 33 L21 38 L28 35 Z" fill="#fff"/></svg>
  <div class="name">OTHER SERVICES</div>
</div>

<section>
  <svg class="abs slide-arrow" style="left:109px" viewBox="0 0 10 74"><path d="M8 1 L2 37 L8 73" stroke="var(--accent)" stroke-width="1.3" fill="none"/></svg>
  <h2 class="abs display slide-title">VoIP PBX solutions for businesses large and small.</h2>
  <div class="abs slide-photo" role="img" aria-label="Glowing world map with network connection arcs"></div>
  <svg class="abs slide-arrow" style="left:738px" viewBox="0 0 10 74"><path d="M2 1 L8 37 L2 73" stroke="var(--accent)" stroke-width="1.3" fill="none"/></svg>
</section>

<main class="abs products">
  <h2 class="display section-title">LATEST PRODUCTS AND SERVICES</h2>
  <article class="product" style="top:41px">
    <div class="thumb" role="img" aria-label="Desk IP telephone"></div>
    <h3>VoIP TELEPHONE</h3>
    <p>Lorem ipsum dolor sit amet, consectetur adipiscing elit, sed do eiusmod tempor incididunt ut labore et dolore magna aliqua. Ut enim ad minim veniam, quis nostrud exercitation ullamco laboris nisi ut aliquip ex ea commodo consequat.</p>
    <a class="more" style="top:86px">Read More</a>
    <div class="rule" style="top:108px"></div>
  </article>
  <article class="product" style="top:166px">
    <div class="thumb" role="img" aria-label="Desk IP telephone"></div>
    <h3>LAN AND INTERNET</h3>
    <p>Lorem ipsum dolor sit amet, consectetur adipiscing elit, sed do eiusmod tempor incididunt ut labore et dolore magna aliqua. Ut enim ad minim veniam, quis nostrud exercitation ullamco laboris nisi ut aliquip ex ea commodo consequat.</p>
    <a class="more" style="top:86px">Read More</a>
    <div class="rule" style="top:112px"></div>
  </article>
  <article class="product" style="top:297px">
    <div class="thumb" role="img" aria-label="Desk IP telephone"></div>
    <h3>SUPPORT SERVICES</h3>
    <p>Lorem ipsum dolor sit amet, consectetur adipiscing elit, sed do eiusmod tempor incididunt ut labore et dolore magna aliqua. Ut enim ad minim veniam, quis nostrud exercitation ullamco laboris nisi ut aliquip ex ea commodo consequat.</p>
    <a class="more" style="top:83px">Read More</a>
    <div class="rule" style="top:111px"></div>
  </article>
</main>

<aside class="abs sidebar">
  <h2 class="display section-title">POPULAR ARTICLES</h2>
  <ul class="articles">
    <li>Lorem ipsum dolor sit amet, consectetur adipiscing elit.</li>
    <li>Lorem ipsum dolor sit amet, consectetur adipiscing elit.</li>
    <li>Lorem ipsum dolor sit amet, consectetur adipiscing elit.</li>
    <li>Lorem ipsum dolor sit amet, consectetur adipiscing elit.</li>
  </ul>
  <h2 class="display section-title" style="margin-top:8px">FOLLOW US</h2>
  <div class="social" style="margin-top:8px"><span></span><span></span><span></span><span></span></div>
  <h2 class="display section-title" style="margin-top:20px">CONTACT US</h2>
  <form style="margin-top:10px">
    <div class="field">NAME</div>
    <div class="field">EMAIL</div>
    <div class="field">PHONE</div>
    <div class="send">SEND</div>
  </form>
</aside>

<div class="abs texture"></div>
<footer class="abs footer">
  <div class="f-col" style="left:105px"><h4>About</h4><ul><li>Homepage</li><li>How we help</li><li>Solutions</li><li>Support Services</li><li>Press Releases</li><li>Video</li></ul></div>
  <div class="f-col" style="left:247px"><h4>Privacy &amp; Security</h4><ul><li>Privacy Policy</li><li>Terms of Use</li><li>Refund Policy</li><li>About Us</li></ul></div>
  <div class="f-col" style="left:391px"><h4>Contact</h4><ul><li>Contact Us</li><li>Ask the Experts</li><li>Follow us on Friendlink</li><li>About Us</li></ul></div>
  <div class="f-social"><span></span><span></span><span></span><span></span></div>
  <p class="copyright">© 2010-2012 MarbleQuay.example - All rights reserved. Reproduction without permission is prohibited</p>
</footer>

</body>
</html>
```